Business Card Design Project

Use our current logo. Clean design.

Industry/Entity Type

Business

Requirements
Must have
• Marisela DUBRANCQ
M. Law
Managing Partner

Alpenvorsa AG
Kornhalmweg 214
CH-3097 Liebefeld

M. +41 79 412 56 27
T. +41 31 928 44 10
F. +41 31 928 44 19

m.dubrancq@alpenvorsa-example.com
www.alpenvorsa-example.com

```html
<!DOCTYPE html>
<html lang="en">
<head>
<meta charset="utf-8">
<title>Alpenvorsa AG – Business Card</title>
<link rel="stylesheet" href="https://fonts.googleapis.com/css2?family=Open+Sans:wght@400;600;700&display=swap">
<style>
  :root {
    --page-bg: #e9e7e3;
    --card-top: #3a3a3a;
    --card-bottom: #262626;
    --ink-light: #e6e6e6;
    --ink-soft: #cfcfcf;
    --swoosh: #d9d9d9;
    --shadow: rgba(0, 0, 0, 0.28);
  }
  * { margin: 0; padding: 0; box-sizing: border-box; }
  html, body {
    width: 1200px;
    height: 960px;
    overflow: hidden;
    background: var(--page-bg);
    font-family: "Open Sans", Arial, sans-serif;
  }
  .canvas {
    position: relative;
    width: 1200px;
    height: 960px;
  }
  .card {
    position: absolute;
    left: 310px;
    width: 580px;
    height: 360px;
    background: linear-gradient(160deg, var(--card-top), var(--card-bottom));
    box-shadow: 0 14px 30px var(--shadow);
    overflow: hidden;
    color: var(--ink-light);
  }
  .card--back { top: 90px; }
  .card--front { top: 510px; }

  /* Back: contact side */
  .brand-small {
    position: absolute;
    top: 34px;
    right: 38px;
    font-size: 17px;
    font-weight: 400;
    letter-spacing: 2px;
    color: var(--ink-light);
  }
  .person {
    position: absolute;
    left: 48px;
    top: 150px;
    line-height: 1.25;
  }
  .person__name { font-size: 21px; font-weight: 400; margin-bottom: 4px; }
  .person__degree { font-size: 20px; font-weight: 700; }
  .person__role { font-size: 17px; font-weight: 400; }
  .person__address { font-size: 15px; color: var(--ink-soft); line-height: 1.4; }
  .contact {
    position: absolute;
    left: 330px;
    top: 160px;
    font-size: 12.5px;
    line-height: 1.55;
    color: var(--ink-soft);
    list-style: none;
  }
  .swoosh {
    position: absolute;
    left: 0;
    bottom: 0;
    width: 580px;
    height: 360px;
  }

  /* Front: brand side */
  .brand-large {
    position: absolute;
    left: 0;
    right: 0;
    top: 148px;
    text-align: center;
    font-size: 46px;
    font-weight: 400;
    letter-spacing: 6px;
    color: var(--ink-light);
  }
</style>
</head>
<body>
<main class="canvas">
  <section class="card card--back" aria-label="Card back with contact details">
    <div class="brand-small">ALPENVORSA</div>

    <div class="person">
      <p class="person__name">Marisela DUBRANCQ</p>
      <p class="person__degree">M. Law</p>
      <p class="person__role">Managing Partner</p>
      <p class="person__address">Alpenvorsa AG<br>Kornhalmweg 214<br>CH-3097 Liebefeld</p>
    </div>

    <ul class="contact">
      <li>M.&nbsp; +41 79 412 56 27</li>
      <li>T.&nbsp; +41 31 928 44 10</li>
      <li>F.&nbsp; +41 31 928 44 19</li>
      <li>m.dubrancq@alpenvorsa-example.com</li>
      <li>www.alpenvorsa-example.com</li>
    </ul>

    <svg class="swoosh" viewBox="0 0 580 360" aria-hidden="true">
      <path d="M0 318 C 200 312, 420 290, 580 258 C 430 298, 220 318, 0 322 Z" fill="var(--swoosh)"/>
    </svg>
  </section>

  <section class="card card--front" aria-label="Card front with company name">
    <div class="brand-large">ALPENVORSA</div>
  </section>
</main>
</body>
</html>
```